Business Card Design

We are looking for a business card designed for our landscaping company. We do landscaping installation & Maintenance Services. We would like to see designs that have basic landscaping in background. We also think it is important to have both of our names and phone numbers on the card. We need something that stands out a little whether it is shape of the card or thickness or design.

Industry/Entity Type

Business

Contact Information for Business Card

Prairie Oak Yardworks, prairieoakyard@mailbox-demo.net, Dale Pruitt 555-613-2907, Marcus Delgado 555-287-4163

```html
<!DOCTYPE html>
<html lang="en">
<head>
<meta charset="utf-8">
<title>Prairie Oak Yardworks – Business Card</title>
<link rel="stylesheet" href="https://fonts.googleapis.com/css2?family=Arimo:wght@400;700&display=swap">
<style>
  :root {
    --page: #ececec;
    --card: #ffffff;
    --lime: #8dc63f;
    --lime-dark: #6fa82a;
    --grass-deep: #3f8a2a;
    --ink: #222222;
    --ink-soft: #3a3a3a;
    --machine-dark: #2b2f2b;
  }
  * { margin: 0; padding: 0; box-sizing: border-box; }
  html, body {
    width: 1200px; height: 837px; overflow: hidden;
    background: var(--page);
    font-family: "Arimo", Arial, sans-serif;
  }
  .card {
    position: absolute; left: 40px; top: 82px;
    width: 1120px; height: 673px;
    background: var(--card);
    overflow: hidden;
  }
  .mower-art {
    position: absolute; left: 21px; top: 26px;
    width: 290px; height: 192px;
    border-radius: 28px 28px 40px 40px;
    background: linear-gradient(135deg, var(--machine-dark) 0%, #4a5a3a 35%, #b6e23a 70%, #8cc21f 100%);
  }
  .name-band {
    position: absolute; left: 280px; top: 135px;
    width: 840px; height: 77px;
  }
  .name-band svg { position: absolute; inset: 0; }
  .company-name {
    position: absolute; left: 72px; top: 0; height: 77px;
    line-height: 77px;
    font-weight: 700; font-size: 48px; color: var(--ink);
    white-space: nowrap;
  }
  .tagline {
    position: absolute; left: 56px; top: 250px;
    font-weight: 700; font-size: 44px; color: var(--lime);
    white-space: nowrap;
  }
  .contacts {
    position: absolute; right: 90px; top: 362px;
    list-style: none; text-align: right;
    font-size: 30px; color: var(--ink-soft);
  }
  .contacts li {
    height: 53px; line-height: 44px;
    display: flex; justify-content: flex-end; align-items: center; gap: 10px;
  }
  .contacts .person { margin-right: 14px; }
  .contacts svg { width: 26px; height: 26px; flex: none; }
  .grass-art {
    position: absolute; left: 0; top: 520px;
    width: 1120px; height: 113px;
    background: linear-gradient(to bottom, rgba(111,168,42,0) 0%, rgba(111,168,42,0.55) 35%, var(--grass-deep) 100%);
  }
  .ground-band {
    position: absolute; left: 0; bottom: 0;
    width: 1120px; height: 40px;
    background: var(--lime);
  }
</style>
</head>
<body>
  <main class="card">
    <div class="mower-art" role="img" aria-label="Illustration of a green push lawn mower"></div>

    <div class="name-band">
      <svg viewBox="0 0 840 77" width="840" height="77" aria-hidden="true">
        <polygon points="30,0 840,0 840,77 0,77" fill="var(--lime)"/>
      </svg>
      <h1 class="company-name">Prairie Oak Yardworks</h1>
    </div>

    <p class="tagline">Landscaping installation &amp; Maintenance</p>

    <ul class="contacts">
      <li>
        <svg viewBox="0 0 26 26" aria-hidden="true">
          <rect x="2" y="6" width="22" height="15" fill="none" stroke="var(--lime)" stroke-width="2"/>
          <polyline points="2,6 13,15 24,6" fill="none" stroke="var(--lime)" stroke-width="2"/>
        </svg>
        <span class="email">prairieoakyard@mailbox-demo.net</span>
      </li>
      <li>
        <span class="person">Dale Pruitt</span>
        <svg viewBox="0 0 26 26" aria-hidden="true">
          <path d="M7 3 L11 8 L9 11 Q11 16 15 18 L18 16 L23 20 L20 24 Q6 22 3 6 Z" fill="var(--lime)"/>
        </svg>
        <span class="phone">555-613-2907</span>
      </li>
      <li>
        <span class="person">Marcus Delgado</span>
        <svg viewBox="0 0 26 26" aria-hidden="true">
          <path d="M7 3 L11 8 L9 11 Q11 16 15 18 L18 16 L23 20 L20 24 Q6 22 3 6 Z" fill="var(--lime)"/>
        </svg>
        <span class="phone">555-287-4163</span>
      </li>
    </ul>

    <div class="grass-art" role="img" aria-label="Illustrated row of green grass blades along the bottom"></div>
    <div class="ground-band"></div>
  </main>
</body>
</html>
```